Paul Sefton Personal Card

I am looking for a personal card that has my contact information on the front and then the url for my website on the back. I am a fan of minimal, modern design, but am very open minded to other styles. Both portrait and landscape designs are acceptable. The only other specification that I have is that some sort of graphic of a raven is present somewhere on the card (my last name 'Sefton' means raven in German).
Contact Information for Business Card
Paul Sefton
608.554.1893
paulwsefton@postvane.net
paulwsefton.com
Colors
Designer to choose colors to be used in the design.
Requirements
Must have
- Raven on some part of the card

```html
<!DOCTYPE html>
<html lang="en">
<head>
<meta charset="utf-8">
<title>Paul Sefton Personal Card</title>
<link rel="stylesheet" href="https://fonts.googleapis.com/css2?family=Oswald:wght@500;600&family=Arimo:wght@400&display=swap">
<style>
  :root {
    --canvas: #e4e4e4;
    --ink: #161616;
    --card-black: #050505;
    --card-white-top: #ffffff;
    --card-white-bottom: #dedede;
    --paper: #f7f7f7;
    --muted: #7a7a7a;
  }
  * { box-sizing: border-box; margin: 0; padding: 0; }
  html, body {
    width: 1200px; height: 1200px; overflow: hidden;
    background: var(--canvas);
  }
  .canvas {
    width: 1200px; height: 1200px;
    display: flex; flex-direction: column; align-items: center; justify-content: center;
    gap: 60px;
  }
  .card {
    width: 840px; height: 480px; position: relative;
    box-shadow: 0 18px 40px rgba(0,0,0,0.22);
  }
  /* Back */
  .card--back {
    background: var(--card-black);
    display: flex; flex-direction: column; align-items: center; justify-content: center;
    gap: 22px;
  }
  .back-raven {
    width: 92px; height: 120px;
    background: var(--paper);
    border-radius: 46px 46px 10px 10px;
  }
  .back-name {
    font-family: "Oswald", sans-serif; font-weight: 600;
    font-size: 30px; letter-spacing: 0.32em; color: var(--paper);
    text-transform: uppercase; padding-left: 0.32em;
  }
  /* Front */
  .card--front {
    background: linear-gradient(160deg, var(--card-white-top) 20%, var(--card-white-bottom) 100%);
  }
  .front-name {
    position: absolute; left: 80px; top: 150px;
    font-family: "Oswald", sans-serif; font-weight: 600;
    font-size: 36px; letter-spacing: 0.3em; color: var(--ink);
    text-transform: uppercase;
  }
  .front-raven {
    position: absolute; left: 560px; top: 95px;
    width: 200px; height: 130px;
    background: var(--ink);
    border-radius: 60px 20px 30px 40px;
  }
  .front-raven-shadow {
    position: absolute; left: 580px; top: 230px;
    width: 150px; height: 22px; border-radius: 50%;
    background: radial-gradient(ellipse at center, rgba(0,0,0,0.18), rgba(0,0,0,0) 70%);
  }
  .contact {
    position: absolute; left: 80px; bottom: 70px;
    list-style: none;
    font-family: "Arimo", sans-serif; font-size: 21px; color: var(--ink);
    display: flex; flex-direction: column; gap: 6px;
  }
  .contact-item { display: flex; align-items: center; gap: 10px; }
  .contact-icon { width: 16px; height: 16px; flex: none; }
  .contact-item--phone { padding-left: 0; }
</style>
</head>
<body>
<main class="canvas">
  <section class="card card--back" aria-label="Card back">
    <div class="back-raven" role="img" aria-label="White raven silhouette perched"></div>
    <p class="back-name">Paul Sefton</p>
  </section>

  <section class="card card--front" aria-label="Card front">
    <h1 class="front-name">Paul Sefton</h1>
    <div class="front-raven-shadow"></div>
    <div class="front-raven" role="img" aria-label="Black raven silhouette standing"></div>
    <ul class="contact">
      <li class="contact-item contact-item--phone">608.554.1893</li>
      <li class="contact-item">
        <svg class="contact-icon" viewBox="0 0 16 16" aria-hidden="true">
          <rect x="1" y="3.5" width="14" height="9" fill="none" stroke="#7a7a7a" stroke-width="1.2"/>
          <path d="M1 3.5 L8 9 L15 3.5" fill="none" stroke="#7a7a7a" stroke-width="1.2"/>
        </svg>
        paulwsefton@postvane.net
      </li>
      <li class="contact-item">
        <svg class="contact-icon" viewBox="0 0 16 16" aria-hidden="true">
          <circle cx="8" cy="8" r="6.5" fill="none" stroke="#7a7a7a" stroke-width="1.2"/>
          <ellipse cx="8" cy="8" rx="3" ry="6.5" fill="none" stroke="#7a7a7a" stroke-width="1"/>
          <path d="M1.5 8 H14.5 M3 4.5 H13 M3 11.5 H13" stroke="#7a7a7a" stroke-width="1"/>
        </svg>
        paulwsefton.com
      </li>
    </ul>
  </section>
</main>
</body>
</html>
```